Nordisk Boligkontor

Company is in: Denmark - Copenhagen
It sells: Restaurants and café buildings
Companys age: 25 years
Main benefit: trust with over 25 years experience

```html
<!DOCTYPE html>
<html lang="da">
<head>
<meta charset="utf-8">
<title>Nordisk Boligkontor</title>
<link href="https://fonts.googleapis.com/css2?family=EB+Garamond:ital,wght@0,500;0,600;1,400&family=Noto+Sans:wght@400;700&display=swap" rel="stylesheet">
<style>
  :root {
    --page: #000000;
    --frame: #3a3128;
    --band: #17130f;
    --gold: #8a7d6a;
    --gold-light: #d9cdb5;
    --cream: #e9dfcc;
    --muted: #6b6156;
    --title-dark: #3b342d;
    --body-text: #e2d7c2;
    --warm: #c98a3a;
  }
  * { box-sizing: border-box; margin: 0; padding: 0; }
  html, body { width: 1200px; height: 900px; overflow: hidden; background: var(--page); }
  body { font-family: "Noto Sans", sans-serif; position: relative; }

  .site { position: absolute; left: 150px; top: 0; width: 900px; height: 782px; border: 1px solid var(--frame); border-top: none; border-radius: 0 0 8px 8px; overflow: hidden; background: #0c0a08; }

  .hero { position: absolute; left: 0; top: 0; width: 900px; height: 375px;
    background: radial-gradient(ellipse at 35% 55%, #b88a4a 0%, #6e4a22 22%, #2a1c10 50%, #0d0905 80%); }
  .hero-city { position: absolute; inset: 0;
    background: linear-gradient(90deg, rgba(120,80,35,.55) 0%, rgba(30,20,10,.2) 45%, rgba(140,90,40,.45) 75%, rgba(20,14,8,.4) 100%); }
  .hero-top { position: absolute; left: 0; top: 0; width: 900px; height: 85px;
    background: linear-gradient(180deg, #1c1915 0%, #0d0b09 100%); border-bottom: 1px solid #4a4036; opacity: .93; }
  .hero-strip { position: absolute; left: 0; top: 333px; width: 900px; height: 42px; background: rgba(12,10,8,.72); }

  .login { position: absolute; left: 36px; top: 21px; }
  .login-field { display: block; width: 148px; height: 18px; margin-bottom: 6px; border: 1px solid #9a8f80; border-radius: 9px;
    background: #141210; color: var(--cream); font-size: 10px; line-height: 16px; padding-left: 9px; letter-spacing: .5px; }
  .login-button { position: absolute; left: 156px; top: 0; width: 53px; height: 18px; border-radius: 9px;
    background: linear-gradient(180deg, #c4b8a4, #6d6457); border: 1px solid #a99d8a; color: #1b1713; font-size: 10px; font-weight: 700; text-align: center; line-height: 16px; }

  .brand-tag { position: absolute; left: 399px; top: 21px; font-size: 10px; letter-spacing: 1px; color: var(--muted); }
  .brand-name { position: absolute; left: 397px; top: 28px; font-family: "EB Garamond", serif; font-weight: 600; font-size: 35px; letter-spacing: .5px; color: var(--gold); white-space: nowrap; }
  .hero-claim { position: absolute; right: 36px; top: 88px; font-family: "EB Garamond", serif; font-style: italic; font-size: 24px; color: var(--cream); }
  .hero-offer { position: absolute; left: 36px; top: 336px; font-family: "EB Garamond", serif; font-style: italic; font-size: 24px; color: var(--cream); }

  .nav { position: absolute; left: 0; top: 375px; width: 900px; height: 75px;
    background: linear-gradient(180deg, #2b241e 0%, #1a1612 45%, #2e251c 100%); border-top: 1px solid #6d5a45; border-bottom: 2px solid #7a5a38; }
  .nav ul { list-style: none; display: flex; height: 100%; align-items: center; }
  .nav li { font-size: 10px; letter-spacing: .6px; color: var(--cream); text-align: center; height: 40px; line-height: 40px; }
  .nav li + li { border-left: 1px solid #8a7c6a; }
  .nav li.is-current { color: var(--muted); }

  .welcome { position: absolute; left: 0; top: 450px; width: 900px; height: 297px; background: linear-gradient(180deg, #231e19 0%, #0d0b09 60%, #0b0908 100%); }
  .welcome-photo { position: absolute; left: 0; top: 0; width: 395px; height: 297px;
    background: linear-gradient(90deg, rgba(150,110,60,.75) 0%, rgba(95,70,40,.6) 45%, rgba(35,28,20,.4) 80%, rgba(12,10,8,0) 100%),
                radial-gradient(ellipse at 40% 60%, #c89a52 0%, #4a3622 55%, #120e0a 100%); }
  .welcome-heading { position: absolute; left: 400px; top: 68px; width: 470px; text-align: center; font-family: "EB Garamond", serif; color: var(--title-dark); }
  .welcome-heading .small { display: block; font-size: 25px; line-height: 28px; font-weight: 500; }
  .welcome-heading .tiny { display: block; font-size: 23px; line-height: 28px; }
  .welcome-heading .big { display: block; font-size: 37px; line-height: 48px; font-weight: 600; white-space: nowrap; }
  .welcome-rule { position: absolute; left: 380px; top: 222px; width: 520px; height: 1px; background: linear-gradient(90deg, transparent, #3e352c 20%, #3e352c); }
  .welcome-text { position: absolute; left: 400px; top: 235px; width: 470px; text-align: center; font-size: 10px; line-height: 13px; color: var(--body-text); }
  .welcome-text strong { color: var(--gold-light); }

  .footer { position: absolute; left: 0; top: 747px; width: 900px; height: 35px; border-top: 2px solid #3e352c; background: #0b0908;
    text-align: center; font-size: 9px; letter-spacing: .5px; color: var(--muted); line-height: 30px; }
</style>
</head>
<body>
<div class="site">
  <header class="hero">
    <div class="hero-city" role="img" aria-label="Nattebillede af oplyste kontor- og restaurationsbygninger i en storby"></div>
    <div class="hero-top"></div>
    <div class="hero-strip"></div>
    <form class="login">
      <span class="login-field">Bruger ...</span>
      <span class="login-field">Kodeord ...</span>
      <span class="login-button">Log in</span>
    </form>
    <p class="brand-tag">salg og udlejning til restaurationsbranchen</p>
    <h1 class="brand-name">NORDISK BOLIGKONTOR</h1>
    <p class="hero-claim">... har over 25 års erfaring i branchen</p>
    <p class="hero-offer">sælge eller købe en restaurationsvirksomhed ...</p>
  </header>

  <nav class="nav">
    <ul>
      <li class="is-current" style="width:137px">Forside</li>
      <li style="width:156px">Firmainfo</li>
      <li style="width:145px">Salgsliste</li>
      <li style="width:181px">Links/Download</li>
      <li style="width:154px">Nyhedsbrev</li>
      <li style="width:127px">Kontakt</li>
    </ul>
  </nav>

  <main class="welcome">
    <div class="welcome-photo" role="img" aria-label="Café med gæster ved runde borde i varmt aftenlys"></div>
    <h2 class="welcome-heading">
      <span class="small">VELKOMMEN</span>
      <span class="tiny">til</span>
      <span class="big">NORDISK BOLIGKONTOR</span>
    </h2>
    <div class="welcome-rule"></div>
    <p class="welcome-text"><strong>NORDISK BOLIGKONTOR</strong> har over 25 års erfaring i branchen, det har givet os et grundigt kendskab til branchens mange spidsfindigheder, og vi kan derfor med sikkerhed sige, at De vil være i gode hænder hos <strong>NORDISK BOLIGKONTOR</strong>, hvad enten De ønsker at sælge eller købe en restaurationsvirksomhed.</p>
  </main>

  <footer class="footer">Copyright © 2011 NORDISK BOLIGKONTOR. All rights reserved</footer>
</div>
</body>
</html>
```